Lose Up To 1 LB Of Fat Per Day

We need a double sided street sign for our weight loss clinic. We need the doctors picture to the right side of the sign and we need a challenge “Lose Up To 1 Pound Of Fat Per Day” included in the signage.
Our color scheme for the clinic are black, white, teal and silver.
The phone number should be at the bottom of the sign
555-206–3948

Target Market(s)

Weight Loss

Font styles to use
Sans Serif

```html
<!DOCTYPE html>
<html lang="en">
<head>
<meta charset="utf-8">
<title>Weight Loss Clinic Street Sign</title>
<link href="https://fonts.googleapis.com/css2?family=Teko:wght@400;500;600&display=swap" rel="stylesheet">
<style>
  :root {
    --stage: #034a4b;
    --teal-deep: #07866f;
    --teal-mid: #0fb592;
    --teal-glow: #1ff5e0;
    --cyan-text: #3ff7ea;
    --ink: #0b3f45;
    --white: #ffffff;
    --suit: #2b3a3a;
    --skin-tone: #8a8f86;
    --accent: #13c79c;
  }
  * { margin: 0; padding: 0; box-sizing: border-box; }
  html, body { width: 1041px; height: 1200px; overflow: hidden; }
  body { background: var(--stage); position: relative; font-family: "Teko", sans-serif; }

  .sign {
    position: absolute; left: 40px; top: 333px;
    width: 960px; height: 534px; overflow: hidden;
    background:
      radial-gradient(ellipse 420px 200px at 62% 0%, var(--teal-glow) 0%, rgba(31,245,224,0) 70%),
      linear-gradient(180deg, var(--teal-mid) 0%, #0a9f84 60%, var(--teal-deep) 100%);
  }
  .sign__ghost {
    position: absolute; left: 10px; top: -40px;
    font-size: 300px; line-height: 230px; font-weight: 600;
    color: rgba(4, 90, 80, 0.18); white-space: nowrap; letter-spacing: 4px;
  }
  .sign__scale-art {
    position: absolute; left: 440px; top: 150px; width: 220px; height: 255px;
    border-radius: 40px 40px 70px 70px;
    background: linear-gradient(160deg, #c9d6d3 0%, #3a4a4a 40%, #d9e07a 80%, #eef07a 100%);
    opacity: 0.9;
  }
  .sign__headline {
    position: absolute; left: 86px; top: 82px;
    color: var(--white); font-size: 112px; line-height: 99px; font-weight: 400;
    transform: skewX(-6deg); letter-spacing: -1px; white-space: nowrap;
    text-shadow: 0 2px 6px rgba(0,60,50,0.35);
  }
  .sign__headline > .sign__line { display: block; height: 99px; }
  .sign__highlight {
    display: inline-block; margin-left: 10px; padding: 0 10px;
    color: var(--cyan-text);
    background: linear-gradient(90deg, rgba(4,110,100,0.85), rgba(4,110,100,0.35));
    line-height: 80px; height: 80px; vertical-align: top; margin-top: 6px;
  }
  .sign__band {
    position: absolute; left: 0; right: 0; bottom: 0; height: 126px;
    background: var(--white);
  }
  .sign__phone {
    position: absolute; left: 100px; top: 440px;
    display: flex; align-items: center; gap: 16px; z-index: 2;
  }
  .sign__phone-number {
    color: var(--ink); font-size: 66px; line-height: 1; font-weight: 500;
    transform: skewX(-8deg); padding-top: 8px; white-space: nowrap;
  }
  .sign__doctor {
    position: absolute; left: 506px; top: 95px; width: 440px; height: 439px;
    border-radius: 160px 160px 0 0;
    background: linear-gradient(180deg, var(--skin-tone) 0%, #6f7a74 35%, var(--suit) 60%, #1d2a2a 100%);
  }
</style>
</head>
<body>
  <div class="sign">
    <div class="sign__ghost" aria-hidden="true">LOSE UP TO<br>POUND</div>
    <div class="sign__scale-art" role="img" aria-label="Illustration of a bathroom scale with dial and a yellow measuring tape"></div>
    <h1 class="sign__headline">
      <span class="sign__line">LOSE UP TO</span>
      <span class="sign__line">1 POUND OF</span>
      <span class="sign__line">FAT<span class="sign__highlight">PER DAY</span></span>
    </h1>
    <div class="sign__band"></div>
    <div class="sign__doctor" role="img" aria-label="Photo of the clinic doctor in a dark suit, white shirt and blue tie"></div>
    <div class="sign__phone">
      <svg width="50" height="50" viewBox="0 0 50 50" aria-hidden="true">
        <circle cx="25" cy="25" r="22" fill="none" stroke="#13c79c" stroke-width="3"/>
        <path d="M18 14c1.5-1 3-1 3.8.5l2 4c.6 1.2.2 2.3-.8 3l-1.4 1c1 2.6 2.8 4.5 5.2 5.6l1-1.4c.7-1 1.900-1.3 3-.7l4 2c1.4.8 1.5 2.3.5 3.8-1.5 2.2-3.8 3-6.4 2-6-2.3-10.2-6.5-12.3-12.5-.9-2.6-.1-4.9 1.4-7.3z" fill="#13c79c"/>
      </svg>
      <span class="sign__phone-number">555-206–3948</span>
    </div>
  </div>
</body>
</html>
```